Vellora Solutions Website Creation

Create a business website for custom flexible packaging and MDF products. The www.Kestivo.example website is generic page that you can use to create a similar home page for my business.
Specifically: https://www.kestivo.example/packaging/
https://www.kestivo.example/product/mdf-panels/
Domain is Vel-Lora.example
I would like the page to have a more packaging related look than the MDF/wood.

```html
<!DOCTYPE html>
<html lang="en">
<head>
<meta charset="UTF-8">
<title>Vellora Solutions — Custom Flexible Packaging &amp; MDF Products</title>
<link rel="stylesheet" href="https://fonts.googleapis.com/css2?family=Roboto:wght@400;500;700&display=swap">
<style>
:root{
  --navy:#1a2142;
  --navy-deep:#131a36;
  --blue:#2b8ee6;
  --blue-bright:#3aa0f0;
  --ink:#1d2233;
  --muted:#55596a;
  --white:#ffffff;
  --line:#d9dbe2;
}
*{box-sizing:border-box;margin:0;padding:0}
html,body{width:1200px;height:4511px;overflow:hidden;background:var(--white);font-family:"Roboto",Arial,sans-serif;color:var(--ink)}
.page{position:relative;width:1200px;height:4511px;overflow:hidden}
.abs{position:absolute}

/* header */
.site-header{position:absolute;left:0;top:0;width:1200px;height:116px;background:var(--navy);z-index:5}
.brand{position:absolute;left:144px;top:32px;display:flex;align-items:center;gap:12px;color:var(--white);font-size:30px;font-weight:500}
.brand-dot{width:48px;height:48px;border-radius:50%;background:var(--blue)}
.nav{position:absolute;left:528px;top:48px;display:flex;gap:27px;font-size:15px;font-weight:500;color:var(--white)}
.nav .active{border-bottom:2px solid var(--blue);padding-bottom:6px}

/* hero */
.hero{position:absolute;left:0;top:0;width:1200px;height:823px;overflow:hidden}
.hero-photo{position:absolute;inset:0;background:linear-gradient(180deg,#2a3140 0%,#3a4150 40%,#4b5260 70%,#6a6f78 100%)}
.hero-title{position:absolute;top:224px;width:1200px;text-align:center;font-size:63px;font-weight:700;color:var(--white)}
.hero-title span{color:var(--blue-bright)}
.hero-text{position:absolute;top:322px;left:250px;width:700px;text-align:center;font-size:20px;line-height:30px;color:var(--white)}
.btn{position:absolute;height:58px;border-radius:29px;display:flex;align-items:center;gap:14px;padding:0 10px 0 26px;font-size:20px;font-weight:500;color:var(--white)}
.btn .ring{width:38px;height:38px;border-radius:50%;background:var(--white);border:4px solid var(--blue)}
.btn-blue{background:var(--blue)}
.btn-dark{background:var(--navy);border:2px solid var(--blue)}
.hero-arrow{position:absolute;top:346px;width:40px;height:40px;border-radius:50%;border:2px solid var(--white)}
.hero-wave{position:absolute;left:0;top:640px}

/* section heads */
.sec-mark{position:absolute;left:577px;width:46px;height:46px;border-radius:50%;border:7px solid var(--blue)}
.eyebrow{position:absolute;width:1200px;text-align:center;font-size:26px;color:var(--ink)}
.sec-title{position:absolute;width:1200px;text-align:center;font-size:47px;font-weight:700;color:var(--ink)}
.sec-title span{color:var(--blue)}

/* products */
.prod-photo{position:absolute;border-radius:50%;box-shadow:4px 6px 10px rgba(0,0,0,.18)}
.prod-title{position:absolute;font-size:23px;font-weight:700;line-height:30px;color:var(--ink)}
.prod-list{position:absolute;list-style:none;font-size:17px;color:var(--muted)}
.prod-list li{line-height:34px;padding-left:22px;position:relative}
.prod-list li::before{content:"";position:absolute;left:0;top:12px;width:11px;height:11px;border-radius:50%;background:var(--blue)}
.side-arrow{position:absolute;width:46px;height:46px;border-radius:50%;border:2px solid #8a8f9c}
.side-arrow svg{position:absolute;left:13px;top:12px}

/* why */
.why{position:absolute;left:18px;top:1778px;width:1182px;height:596px;border-radius:300px 0 0 300px/300px 0 0 300px;background:linear-gradient(100deg,#16356a 0%,#1d4f92 45%,#2d78c0 100%);overflow:hidden}
.why-eyebrow{position:absolute;left:0;top:1883px;width:1220px;text-align:center;font-size:26px;color:var(--white)}
.why-title{position:absolute;left:0;top:1930px;width:1220px;text-align:center;font-size:47px;font-weight:700;line-height:58px;color:var(--white)}
.why-title span{color:var(--blue-bright)}
.feature{position:absolute;top:2104px;width:170px;text-align:center;color:var(--white);font-size:20px;font-weight:500;line-height:25px}
.feature .ic{width:88px;height:88px;border-radius:50%;border:3px solid var(--white);background:rgba(255,255,255,.08);margin:0 auto 8px;display:flex;align-items:center;justify-content:center}
.feature .ic.on{background:var(--navy)}

/* industries */
.tile{position:absolute;width:279px;height:266px;border-radius:10px;overflow:hidden}
.tile .label{position:absolute;left:8px;right:8px;bottom:8px;height:44px;border-radius:6px;background:rgba(26,33,66,.9);color:var(--white);font-size:18px;display:flex;align-items:center;justify-content:center}
.tile .label.hl{background:var(--blue)}

/* cta */
.cta{position:absolute;left:0;top:3486px;width:1200px;height:596px;background:linear-gradient(90deg,#1a2a56 0%,#1d3a72 60%,#1a2142 100%)}
.cta-eyebrow{position:absolute;left:144px;top:3647px;font-size:25px;color:var(--blue-bright)}
.cta-title{position:absolute;left:144px;top:3695px;font-size:47px;font-weight:700;line-height:58px;color:var(--white)}
.cta-title span{color:var(--blue-bright)}

/* footer */
.foot-h{position:absolute;top:4160px;font-size:25px;font-weight:500;color:var(--ink);border-bottom:2px solid var(--ink);padding-bottom:2px}
.foot-list{position:absolute;top:4232px;list-style:none;font-size:15px;line-height:24px;color:var(--ink)}
.contact li{display:flex;gap:12px;margin-bottom:8px}
.contact svg{flex:none;margin-top:4px}
.news-form{position:absolute;left:806px;top:4292px;width:246px;height:44px;border:1px solid #b9bcc6;border-radius:22px;overflow:hidden;display:flex}
.news-form span{flex:1;font-size:13px;color:var(--muted);padding:13px 0 0 28px}
.news-form b{width:86px;background:var(--blue);color:var(--white);font-size:14px;font-weight:500;display:flex;align-items:center;justify-content:center}
.foot-rule{position:absolute;left:40px;top:4411px;width:1120px;height:1px;background:var(--line)}
.copy{position:absolute;left:144px;top:4454px;font-size:15px;color:var(--ink)}
.social{position:absolute;top:4446px;width:36px;height:36px;border-radius:50%;background:var(--navy-deep)}
</style>
</head>
<body>
<div class="page">

  <!-- Hero -->
  <section class="hero">
    <div class="hero-photo" role="img" aria-label="Packaging warehouse with boxes moving along a roller conveyor"></div>
    <h1 class="hero-title">Built Around <span>Your Product.</span></h1>
    <p class="hero-text">Vellora Solutions delivers custom flexible packaging, roll stock, films, bottles, closures, MDF panels, and industrial packaging solutions designed to help manufacturers improve efficiency and grow their business.</p>
    <a class="btn btn-blue" style="left:340px;top:440px;width:248px">Request a Quote <span class="ring"></span></a>
    <a class="btn btn-dark" style="left:610px;top:440px;width:250px">Explore Products <span class="ring"></span></a>
    <span class="hero-arrow" style="left:80px"></span>
    <span class="hero-arrow" style="left:1080px"></span>
    <svg class="hero-wave" width="1200" height="184" viewBox="0 0 1200 184">
      <path d="M0 40 Q600 290 1200 40 L1200 184 L0 184Z" fill="#fff"/>
      <path d="M0 30 Q600 280 1200 30 L1200 60 Q600 300 0 60Z" fill="#1a2142"/>
      <path d="M0 10 Q600 250 1200 10" stroke="#2b8ee6" stroke-width="12" fill="none"/>
    </svg>
  </section>

  <!-- Header -->
  <header class="site-header">
    <div class="brand"><span class="brand-dot"></span>Vellora Solutions</div>
    <nav class="nav">
      <span class="active">HOME</span><span>ABOUT</span><span>FLEXIBLE PACKAGING</span><span>MDF PANELS</span><span>CONTACT</span>
    </nav>
  </header>

  <!-- Products -->
  <span class="sec-mark" style="top:876px"></span>
  <p class="eyebrow" style="top:948px">Trusted Packaging Partner</p>
  <h2 class="sec-title" style="top:990px">Packaging That <span>Performs</span></h2>

  <span class="side-arrow" style="left:67px;top:1379px"><svg width="16" height="20"><path d="M11 2 L3 10 L11 18" stroke="#8a8f9c" stroke-width="2" fill="none"/></svg></span>
  <span class="side-arrow" style="left:1086px;top:1379px"><svg width="16" height="20"><path d="M5 2 L13 10 L5 18" stroke="#8a8f9c" stroke-width="2" fill="none"/></svg></span>

  <div class="prod-photo" role="img" aria-label="Pasta being filled into flexible pouches on a packaging machine" style="left:148px;top:1143px;width:262px;height:262px;background:radial-gradient(circle at 50% 60%,#c9a46a,#8a8680 60%,#5a5c60)"></div>
  <h3 class="prod-title" style="left:180px;top:1427px">Custom Flexible<br>Packaging</h3>
  <ul class="prod-list" style="left:180px;top:1500px"><li>Stand-up pouches</li><li>Vacuum pouches</li><li>Roll stock</li><li>Shrink bags</li><li>Custom printed films</li></ul>

  <h3 class="prod-title" style="left:479px;top:1135px">Industrial Packaging</h3>
  <ul class="prod-list" style="left:479px;top:1178px"><li>Stretch film</li><li>Machine film</li><li>Banding</li><li>Safety products</li><li>Corrugated packaging</li></ul>
  <div class="prod-photo" role="img" aria-label="Workers on a food packaging line" style="left:472px;top:1381px;width:258px;height:258px;border-radius:50% 0 50% 50%;background:linear-gradient(160deg,#8fb4d6,#3e6e9e 60%,#1e3e66);box-shadow:0 14px 0 -4px #2b8ee6,0 22px 0 -6px #1a2142"></div>

  <div class="prod-photo" role="img" aria-label="Hand holding a fan of MDF and wood veneer samples" style="left:792px;top:1143px;width:262px;height:262px;background:radial-gradient(circle at 50% 50%,#8a6a4a,#b99c7c 55%,#d8d2cc)"></div>
  <h3 class="prod-title" style="left:826px;top:1427px">MDF Products</h3>
  <ul class="prod-list" style="left:826px;top:1470px"><li>Standard MDF</li><li>Industrial Panels</li><li>Custom Sizes</li><li>Building Materials</li></ul>

  <!-- Why -->
  <section class="why" role="img" aria-label="Blue-tinted factory conveyor line in the background"></section>
  <p class="why-eyebrow">Why Vel-Lora</p>
  <h2 class="why-title"><span>One Supplier.</span><br>Endless Packaging Solutions.</h2>

  <div class="feature" style="left:178px"><div class="ic"><svg width="44" height="44" viewBox="0 0 44 44" fill="none" stroke="#fff" stroke-width="2"><circle cx="22" cy="18" r="7"/><circle cx="22" cy="18" r="12" stroke-dasharray="4 3"/><rect x="8" y="32" width="28" height="6"/></svg></div>Custom<br>Manufacturing</div>
  <div class="feature" style="left:353px"><div class="ic"><svg width="44" height="44" viewBox="0 0 44 44" fill="none" stroke="#fff" stroke-width="2"><circle cx="22" cy="22" r="15"/><ellipse cx="22" cy="22" rx="7" ry="15"/><path d="M7 22h30M10 14h24M10 30h24"/></svg></div>Global<br>Sourcing</div>
  <div class="feature" style="left:527px"><div class="ic on"><svg width="44" height="44" viewBox="0 0 44 44" fill="none" stroke="#fff" stroke-width="2"><circle cx="25" cy="22" r="13"/><path d="M25 14v8l6 4M4 18h8M2 24h9M5 30h8"/></svg></div>Fast<br>Lead Times</div>
  <div class="feature" style="left:703px"><div class="ic"><svg width="44" height="44" viewBox="0 0 44 44" fill="none" stroke="#fff" stroke-width="2"><rect x="6" y="8" width="26" height="22"/><circle cx="28" cy="28" r="8"/><path d="M34 34l6 6M10 24l6-6 5 4 7-8"/></svg></div>Competitive<br>Pricing</div>
  <div class="feature" style="left:879px"><div class="ic"><svg width="44" height="44" viewBox="0 0 44 44" fill="none" stroke="#fff" stroke-width="2"><circle cx="24" cy="15" r="8"/><path d="M4 32l8-4h10l8 2 8-6M12 38h16"/></svg></div>Personalized<br>Service</div>

  <!-- Industries -->
  <span class="sec-mark" style="top:2486px"></span>
  <p class="eyebrow" style="top:2557px">We Serve</p>
  <h2 class="sec-title" style="top:2598px">Industries <span>Served</span></h2>

  <div class="tile" style="left:80px;top:2698px" role="img" aria-label="Food processing weighing machine with pasta"><div style="position:absolute;inset:0;background:linear-gradient(160deg,#b89a52,#6a6658)"></div><span class="label">Food Processing</span></div>
  <div class="tile" style="left:366px;top:2698px" role="img" aria-label="Tractor working a field at sunset"><div style="position:absolute;inset:0;background:linear-gradient(180deg,#9aa2b0,#d8a878 45%,#6a4e3a)"></div><span class="label hl">Agriculture</span></div>
  <div class="tile" style="left:652px;top:2698px" role="img" aria-label="White supplement bottles on a production line"><div style="position:absolute;inset:0;background:linear-gradient(180deg,#9fb0c4,#e8ecf0 55%,#7a8898)"></div><span class="label">Nutraceutical</span></div>
  <div class="tile" style="left:938px;top:2698px" role="img" aria-label="Colourful pet food bags"><div style="position:absolute;inset:0;background:linear-gradient(90deg,#e8a040,#4aa0d0 50%,#d84a3a)"></div><span class="label">Pet Food</span></div>

  <div class="tile" style="left:-22px;top:2977px" role="img" aria-label="Water bottles on an industrial filling line"><div style="position:absolute;inset:0;background:linear-gradient(180deg,#7a8ea8,#c8d6e4 60%,#4a5a70)"></div><span class="label">Industrial</span></div>
  <div class="tile" style="left:266px;top:2977px" role="img" aria-label="Amber medicine bottles on a conveyor"><div style="position:absolute;inset:0;background:linear-gradient(180deg,#2a2a30,#b86a2a 55%,#3a4050)"></div><span class="label">Medical</span></div>
  <div class="tile" style="left:552px;top:2977px" role="img" aria-label="Milk bottles on a retail production line"><div style="position:absolute;inset:0;background:linear-gradient(180deg,#6a7a88,#e8e6dc 55%,#5a6674)"></div><span class="label">Retail</span></div>
  <div class="tile" style="left:838px;top:2977px" role="img" aria-label="Beverage cans on a conveyor"><div style="position:absolute;inset:0;background:linear-gradient(180deg,#3a2a20,#8a4a2a 40%,#2a2e36)"></div><span class="label">Beverage</span></div>

  <a class="btn btn-blue" style="left:497px;top:3294px;width:207px;height:60px">View More <span class="ring"></span></a>

  <!-- CTA -->
  <div class="abs" style="left:0;top:3481px;width:1200px;height:5px;background:#cfd2da"></div>
  <section class="cta">
    <svg class="abs" style="left:600px;top:20px" width="600" height="560" viewBox="0 0 600 560">
      <path d="M430 10 A270 270 0 1 1 150 520" stroke="#2b8ee6" stroke-width="40" fill="none"/>
      <path d="M170 100 A230 230 0 0 1 500 70" stroke="#3aa0f0" stroke-width="18" fill="none"/>
      <circle cx="285" cy="278" r="232" fill="#131a36"/>
    </svg>
    <div class="abs" role="img" aria-label="Smiling worker in a hard hat holding a tablet" style="left:670px;top:93px;width:430px;height:430px;border-radius:50%;background:radial-gradient(circle at 45% 40%,#d8b070,#9a6a40 45%,#3a3a44)"></div>
  </section>
  <p class="cta-eyebrow">Request A Quote</p>
  <h2 class="cta-title">Let's Build Better<br><span>Packaging Together</span></h2>
  <a class="btn btn-blue" style="left:147px;top:3850px;width:240px;height:60px">Request Quote <span class="ring"></span></a>

  <!-- Footer -->
  <footer>
    <h4 class="foot-h" style="left:140px">Contact Us</h4>
    <ul class="foot-list contact" style="left:140px;width:240px">
      <li><svg width="12" height="16" viewBox="0 0 12 16"><path d="M6 0a6 6 0 0 1 6 6c0 4-6 10-6 10S0 10 0 6a6 6 0 0 1 6-6z" fill="#2b8ee6"/><circle cx="6" cy="6" r="2" fill="#fff"/></svg><span>233,Sed ut perspiciatis unde mnis iste nvoluptatem</span></li>
      <li><svg width="13" height="13" viewBox="0 0 13 13"><path d="M2 0l3 3-1.5 2a8 8 0 0 0 4.5 4.5L10 8l3 3-2 2C5 13 0 8 0 2z" fill="#2b8ee6"/></svg><span>Phone : +1 888 888 8888</span></li>
      <li><svg width="13" height="10" viewBox="0 0 13 10"><rect width="13" height="10" fill="#2b8ee6"/><path d="M0 0l6.5 5L13 0" stroke="#fff" fill="none"/></svg><span>info@companyname.com</span></li>
    </ul>
    <h4 class="foot-h" style="left:427px">Menus</h4>
    <ul class="foot-list" style="left:428px"><li>Home</li><li>About</li><li>Flexible Packaging</li><li>MDF Panels</li><li>Contact</li></ul>
    <h4 class="foot-h" style="left:634px">Links</h4>
    <ul class="foot-list" style="left:636px"><li>Privacy Policy</li><li>Terms of Use</li><li>Sitemap</li><li>Information</li></ul>
    <h4 class="foot-h" style="left:804px">Sign Up to Newsletter</h4>
    <p class="foot-list" style="left:806px;width:270px">Sed ut perspiciatis unde omnis iste natus error sit voluptatem</p>
    <div class="news-form"><span>Enter Email</span><b>SIGN UP</b></div>
    <div class="foot-rule"></div>
    <p class="copy">© 2026 Companyname. All rights reserved &nbsp;|&nbsp; Privacy &nbsp;|&nbsp; Terms of Use</p>
    <span class="social" style="left:825px"></span>
    <span class="social" style="left:873px"></span>
    <span class="social" style="left:921px;background:var(--blue)"></span>
    <span class="social" style="left:969px"></span>
    <span class="social" style="left:1017px"></span>
  </footer>
</div>
</body>
</html>
```